Enterprise Application UI beautification

We have an enterprise application that is being redesigned. A screenshot from the new UX/UI is provided. The current UI design is OK but we would like it to look better. The key goals of the UI are to look like a premium product (think luxury brand) and for it to be visually very appealing/attractive. When people see the UI we want them to have a significant, positive reaction. They should "ooh" and "ahh". This is a product sold to large enterprises, not consumers. The current UI is a little plain. The colors we want to use are blue, yellow, black, white and gray. We probably don't want different colors but feel free to use any variations within or close to that color scheme that you see fit. Also feel free to modify the spacing, icons, widgets, tables, fonts, etc.

Target Market(s)

Large enterprise customers (Summit 300).

Number of Pages Required

1 page

Font styles to use
Sans Serif

Colors
3277b5

Requirements
Must have
• A premium feel.

```html
<!DOCTYPE html>
<html lang="en">
<head>
<meta charset="utf-8">
<title>Data Sources</title>
<link href="https://fonts.googleapis.com/css2?family=Poppins:wght@400;500;600;700&display=swap" rel="stylesheet">
<style>
:root{
  --blue:#3277b5;
  --blue-dark:#2a67a3;
  --navy:#0d3868;
  --navy-table:#1a4c86;
  --yellow:#f5b82e;
  --ink:#16181d;
  --gray:#6b7280;
  --gray-light:#c5ccd6;
  --line:#e6e9ee;
  --canvas:#f4f6f9;
  --white:#ffffff;
  --red:#e5533d;
  --red-soft:#fde7e3;
  --green:#3ccf7c;
}
*{box-sizing:border-box;margin:0;padding:0}
html,body{width:1200px;height:1029px;overflow:hidden}
body{font-family:'Poppins',sans-serif;background:var(--canvas);color:var(--ink);position:relative}
.topbar{position:absolute;left:0;top:0;width:1200px;height:86px;background:linear-gradient(90deg,var(--blue-dark),var(--blue) 60%,#3a82c2)}
.brand-mark{position:absolute;left:18px;top:29px;width:28px;height:28px;border-radius:50%;background:var(--white)}
.page-title{position:absolute;left:95px;top:29px;font-size:20px;font-weight:700;color:var(--white);letter-spacing:.5px;display:flex;align-items:center;gap:8px}
.plus-dot{width:29px;height:29px;border-radius:50%;background:var(--yellow);color:var(--white);display:flex;align-items:center;justify-content:center;font-size:20px;font-weight:500;line-height:1}
.search{position:absolute;left:708px;top:22px;width:305px;height:41px;border-radius:21px;background:rgba(255,255,255,.18);color:rgba(255,255,255,.9);font-size:13.5px;display:flex;align-items:center;padding-left:25px}
.search .sep{position:absolute;right:41px;top:13px;width:1px;height:15px;background:rgba(255,255,255,.35)}
.search svg{position:absolute;right:14px;top:13px}
.user{position:absolute;left:1056px;top:32px;display:flex;align-items:center;gap:6px;color:var(--white);font-weight:600;font-size:14.5px}
.rail{position:absolute;left:0;top:86px;width:70px;height:943px;background:var(--navy)}
.rail-icon{position:absolute;left:20px;width:30px;height:30px}
.rail-active{position:absolute;left:0;top:199px;width:3px;height:28px;background:var(--yellow)}
.source-list{position:absolute;left:70px;top:86px;width:273px;height:943px;background:var(--white)}
.source{position:absolute;left:25px;width:240px}
.source .name{font-size:14px;color:var(--ink);line-height:18px;white-space:nowrap}
.source .kind{font-size:12.5px;color:var(--gray);line-height:17px}
.divider{position:absolute;left:25px;width:223px;height:1px;background:var(--line)}
.scroll{position:absolute;left:263px;top:38px;width:3px;height:132px;background:#eef0f3;border-radius:2px}
.main{position:absolute;left:367px;top:86px;width:806px}
.heading{font-size:26px;font-weight:500;color:var(--ink)}
.detail-title{position:absolute;left:0;top:35px}
.actions{position:absolute;left:346px;top:34px;display:flex;gap:7px}
.pill{height:33px;border-radius:17px;display:flex;align-items:center;justify-content:center;gap:3px;font-size:12px;font-weight:500}
.pill.edit{width:95px;background:#fcefd2;color:var(--yellow)}
.pill.clone{width:96px;background:#dde8f4;color:var(--blue)}
.pill.delete{width:95px;background:var(--red-soft);color:var(--red)}
.pill.test{width:153px;background:#daf5e6;color:var(--green)}
.card{position:absolute;left:1px;width:805px;background:var(--white);border-radius:10px;box-shadow:0 2px 10px rgba(20,40,80,.04)}
.info{top:92px;height:177px}
.info dl{position:absolute;top:24px;display:grid;row-gap:7px;align-items:center}
.info dt{font-size:14px;color:var(--ink);line-height:19px;white-space:nowrap}
.info dd{font-size:13px;color:var(--gray);line-height:19px;white-space:nowrap}
.info .left{left:25px;grid-template-columns:164px 180px}
.info .right{left:437px;grid-template-columns:152px 214px}
.info .vline{position:absolute;left:375px;top:24px;width:1px;height:132px;background:var(--line)}
.objects-title{position:absolute;left:0;top:308px;display:flex;align-items:center;gap:5px}
.account{top:366px;height:283px}
.obj-head{position:absolute;left:18px;top:14px;display:flex;align-items:center;gap:6px;font-size:15px}
.chip{width:29px;height:29px;border-radius:50%;display:flex;align-items:center;justify-content:center}
.chip.remove{background:var(--red-soft)}
.chip.add{background:#e7e9ec}
.fields-label{margin-left:25px}
.chev{position:absolute;right:16px}
.table{position:absolute;left:18px;top:55px;width:770px}
.thead{height:45px;background:var(--navy-table);border-radius:8px;color:var(--white);font-size:13px;font-weight:500;position:relative}
.thead span,.row span{position:absolute;top:50%;transform:translateY(-50%);white-space:nowrap}
.row{position:relative;height:34px;border-bottom:1px solid var(--line);font-size:13px;color:var(--gray)}
.row:last-child{border-bottom:none}
.rows{margin-top:25px}
.c1{left:22px}.c2{left:194px}.c3{left:352px}.c4{left:454px}.c5{left:578px}.c6{left:713px}
.box{width:16px;height:16px;border-radius:4px;background:#eef1f5;left:420px}
.box.on{background:var(--blue)}
.rule{display:flex;align-items:center;gap:6px}
.rule b{font-weight:500;font-size:17px;line-height:1}
.row-actions{position:absolute;left:726px;top:134px;display:grid;grid-template-columns:17px 17px;column-gap:12px;row-gap:18px}
.collapsed{height:51px}
.collapsed .obj-head{top:11px}
.collapsed .chev{top:19px}
</style>
</head>
<body>
<header class="topbar">
  <div class="brand-mark"></div>
  <div class="page-title">DATA SOURCES <span class="plus-dot">+</span></div>
  <div class="search">Search here...<span class="sep"></span>
    <svg width="15" height="15" viewBox="0 0 16 16" fill="none" stroke="#fff" stroke-width="1.6"><circle cx="7" cy="7" r="5"/><path d="M11 11l3.5 3.5"/></svg>
  </div>
  <div class="user">
    <svg width="24" height="24" viewBox="0 0 24 24" fill="#fff"><path d="M12 8.5a3.5 3.5 0 100 7 3.5 3.5 0 000-7zm9 5v-3l-2.4-.5-.7-1.7 1.3-2.1-2.1-2.1-2.1 1.3-1.7-.7L12.8 2h-3l-.5 2.4-1.7.7-2.1-1.3-2.1 2.1 1.3 2.1-.7 1.7L1.5 10.5v3l2.4.5.7 1.7-1.3 2.1 2.1 2.1 2.1-1.3 1.7.7.5 2.4h3l.5-2.4 1.7-.7 2.1 1.3 2.1-2.1-1.3-2.1.7-1.7z"/></svg>
    NORA VANCE
    <svg width="10" height="10" viewBox="0 0 10 10" fill="none" stroke="#fff" stroke-width="1.6"><path d="M2 3.5l3 3 3-3"/></svg>
  </div>
</header>

<nav class="rail">
  <svg class="rail-icon" style="top:36px" viewBox="0 0 30 30" fill="none" stroke="#fff" stroke-width="1.6"><circle cx="15" cy="8" r="3"/><circle cx="7" cy="11" r="2.5"/><circle cx="23" cy="11" r="2.5"/><path d="M10 26v-8a5 5 0 0110 0v8M3 24v-5a4 4 0 014-4M27 24v-5a4 4 0 00-4-4"/></svg>
  <svg class="rail-icon" style="top:118px" viewBox="0 0 30 30" fill="none" stroke="#fff" stroke-width="1.6"><path d="M8 22h15a5 5 0 000-10 7 7 0 00-13-1 5.5 5.5 0 00-2 11z"/></svg>
  <span class="rail-active"></span>
  <svg class="rail-icon" style="top:197px" viewBox="0 0 30 30" fill="none" stroke="#f5b82e" stroke-width="1.8"><rect x="6" y="4" width="19" height="17" rx="2"/><path d="M3 25h24M10 21v4M6 17h19"/></svg>
  <svg class="rail-icon" style="top:278px" viewBox="0 0 30 30" fill="none" stroke="#fff" stroke-width="1.6"><rect x="6" y="5" width="17" height="21" rx="2"/><path d="M11 3h7v4h-7zM10 13h8M10 17h5M16 22l3 3 5-6"/></svg>
  <svg class="rail-icon" style="top:349px" viewBox="0 0 30 30" fill="none" stroke="#fff" stroke-width="1.6"><rect x="4" y="6" width="20" height="19" rx="2"/><path d="M4 11h20M9 3v5M19 3v5"/><circle cx="22" cy="22" r="4.5"/><path d="M22 20v2l1.5 1"/></svg>
  <svg class="rail-icon" style="top:430px" viewBox="0 0 30 30" fill="none" stroke="#fff" stroke-width="1.6"><rect x="4" y="4" width="6" height="6" rx="1"/><circle cx="22" cy="23" r="3.5"/><path d="M7 10v8a5 5 0 005 5h6M22 19v-6a5 5 0 00-5-5h-4"/></svg>
</nav>

<aside class="source-list">
  <div class="scroll"></div>
  <div class="source" style="top:34px"><div class="name">Skyforce- Sandox</div><div class="kind">Skyforce.io</div></div>
  <div class="divider" style="top:93px"></div>
  <div class="source" style="top:115px"><div class="name">Pondbase Test 1 (administration)</div><div class="kind">PondbaseSQL</div></div>
  <div class="divider" style="top:174px"></div>
  <div class="source" style="top:196px"><div class="name">Pondbase Test 2 (administration)</div><div class="kind">PondbaseSQL</div></div>
  <div class="divider" style="top:253px"></div>
  <div class="source" style="top:275px"><div class="name">Sadga</div><div class="kind">Skyforce.io</div></div>
  <div class="divider" style="top:329px"></div>
  <div class="source" style="top:346px"><div class="name">Skyforce Test 1 (administration)</div><div class="kind">PondbaseSQL</div></div>
  <div class="divider" style="top:404px"></div>
  <div class="source" style="top:428px"><div class="name">SKFC - Field Entry Test</div><div class="kind">Skyforce.io</div></div>
  <div class="divider" style="top:486px"></div>
  <div class="source" style="top:508px"><div class="name">SKFC 44</div><div class="kind">Skyforce.io</div></div>
  <div class="divider" style="top:566px"></div>
  <div class="source" style="top:589px"><div class="name">SKFC 66</div><div class="kind">Skyforce.io</div></div>
</aside>

<main class="main">
  <h1 class="heading detail-title">Skyforce - Sandbox</h1>
  <div class="actions">
    <div class="pill edit"><svg width="17" height="17" viewBox="0 0 18 18" fill="none" stroke="#f5b82e" stroke-width="1.6"><path d="M9 3H3v12h12V9M7 11l1-3 7-7 2 2-7 7z"/></svg>EDIT</div>
    <div class="pill clone"><svg width="22" height="15" viewBox="0 0 22 15" fill="none" stroke="#3277b5" stroke-width="1.8"><circle cx="7.5" cy="7.5" r="6"/><circle cx="14.5" cy="7.5" r="6"/></svg>CLONE</div>
    <div class="pill delete"><svg width="14" height="16" viewBox="0 0 14 16" fill="none" stroke="#e5533d" stroke-width="1.6"><path d="M1 3h12M5 3V1h4v2M2.5 3l1 12h7l1-12M5.5 6v6M8.5 6v6"/></svg>DELETE</div>
    <div class="pill test"><svg width="11" height="16" viewBox="0 0 11 16" fill="#3ccf7c"><path d="M7 0L0 9h4l-1 7 8-10H6z"/></svg>TEST CONNECTION</div>
  </div>

  <section class="card info">
    <dl class="left">
      <dt>Data Source Name</dt><dd>Skyforce - Sandbox</dd>
      <dt>Data Source Type</dt><dd>Application</dd>
      <dt>Status</dt><dd>Active</dd>
      <dt>Created By</dt><dd>tamsin.test</dd>
      <dt>Last Updated By</dt><dd>tamsin.test</dd>
    </dl>
    <div class="vline"></div>
    <dl class="right">
      <dt>Username</dt><dd>masterdev@dev.northwind.net</dd>
      <dt>Security Token</dt><dd>tadkaji4234ifndkn3</dd>
      <dt>Environment Type</dt><dd>Production</dd>
      <dt>Connected App</dt><dd>No</dd>
    </dl>
  </section>

  <h2 class="heading objects-title">Data Objects <span class="plus-dot">+</span></h2>

  <section class="card account">
    <div class="obj-head" style="width:770px">Account
      <span class="chip remove"><svg width="10" height="10" viewBox="0 0 10 10" stroke="#e5533d" stroke-width="1.8"><path d="M1 1l8 8M9 1l-8 8"/></svg></span>
      <span class="fields-label">Feilds</span>
      <span class="chip add"><svg width="11" height="11" viewBox="0 0 11 11" stroke="#16181d" stroke-width="1.8"><path d="M5.5 0v11M0 5.5h11"/></svg></span>
      <svg class="chev" style="right:0" width="12" height="12" viewBox="0 0 12 12" fill="none" stroke="#16181d" stroke-width="1.8"><path d="M2 4l4 4 4-4"/></svg>
    </div>
    <div class="table">
      <div class="thead">
        <span class="c1">Feilds Name</span><span class="c2">Data Type</span><span class="c3">Primary Key</span><span class="c4">Rule Type</span><span class="c5">Sensitive Data</span><span class="c6">Actions</span>
      </div>
      <div class="rows">
        <div class="row"><span class="c1">Account description</span><span class="c2">Common.Text</span>
          <span class="box on"><svg width="16" height="16" viewBox="0 0 16 16" fill="none" stroke="#fff" stroke-width="1.8"><path d="M4 8l3 3 5-6"/></svg></span>
          <span class="c4 rule"><b style="color:#16181d">a</b><svg width="11" height="11" viewBox="0 0 11 11" fill="none" stroke="#c5ccd6" stroke-width="1.5"><circle cx="4.5" cy="4.5" r="3.5"/><path d="M7 7l3 3"/></svg><svg width="11" height="11" viewBox="0 0 11 11" fill="none" stroke="#16181d" stroke-width="1.5"><rect x="1" y="4" width="6" height="6"/><rect x="4" y="1" width="6" height="6"/></svg><svg width="30" height="10" viewBox="0 0 30 10" fill="#c5ccd6"><rect x="0" y="1" width="8" height="8" rx="2"/><path d="M16 1l4 4-4 4-4-4z"/><path d="M25 2l5 3-5 3z"/></svg></span>
          <span class="c5" style="left:598px;display:flex;gap:8px"><svg width="44" height="14" viewBox="0 0 44 14" fill="none" stroke="#c5ccd6" stroke-width="1.4"><rect x="1" y="1" width="11" height="12" rx="2"/><path d="M6.5 4v6M3.5 7h6"/><rect x="19" y="2" width="14" height="10" rx="2"/><path d="M19 7h14"/><circle cx="40" cy="4" r="2.5" fill="#c5ccd6"/><path d="M36 13a4 4 0 018 0z" fill="#c5ccd6"/></svg></span></div>
        <div class="row"><span class="c1">Account Fax</span><span class="c2">Address. Address Line 3</span><span class="box"></span>
          <span class="c4 rule"><b style="color:#c5ccd6">a</b><svg width="11" height="11" viewBox="0 0 11 11" fill="none" stroke="#c5ccd6" stroke-width="1.5"><circle cx="4.5" cy="4.5" r="3.5"/><path d="M7 7l3 3"/></svg><svg width="11" height="11" viewBox="0 0 11 11" fill="none" stroke="#16181d" stroke-width="1.5"><rect x="1" y="4" width="6" height="6"/><rect x="4" y="1" width="6" height="6"/></svg><svg width="30" height="10" viewBox="0 0 30 10" fill="#c5ccd6"><rect x="0" y="1" width="8" height="8" rx="2"/><path d="M16 1l4 4-4 4-4-4z"/><path d="M25 2l5 3-5 3z"/></svg></span></div>
        <div class="row"><span class="c1">Account ID</span><span class="c2">Common ID</span><span class="box"></span>
          <span class="c4 rule"><b style="color:#3277b5">a</b><svg width="11" height="11" viewBox="0 0 11 11" fill="none" stroke="#3ccf7c" stroke-width="1.8"><circle cx="4.5" cy="4.5" r="3.5"/><path d="M7 7l3 3"/></svg><svg width="11" height="11" viewBox="0 0 11 11" fill="none" stroke="#c5ccd6" stroke-width="1.5"><rect x="1" y="4" width="6" height="6"/><rect x="4" y="1" width="6" height="6"/></svg><svg width="30" height="10" viewBox="0 0 30 10" fill="#c5ccd6"><rect x="0" y="1" width="8" height="8" rx="2"/><path d="M16 1l4 4-4 4-4-4z"/><path d="M25 2l5 3-5 3z"/></svg></span></div>
        <div class="row"><span class="c1">Account Name</span><span class="c2">Address. Address Line 2</span><span class="box"></span>
          <span class="c4 rule"><b style="color:#c5ccd6">a</b><svg width="11" height="11" viewBox="0 0 11 11" fill="none" stroke="#c5ccd6" stroke-width="1.5"><circle cx="4.5" cy="4.5" r="3.5"/><path d="M7 7l3 3"/></svg><svg width="11" height="11" viewBox="0 0 11 11" fill="none" stroke="#16181d" stroke-width="1.5"><rect x="1" y="4" width="6" height="6"/><rect x="4" y="1" width="6" height="6"/></svg><svg width="30" height="10" viewBox="0 0 30 10" fill="#c5ccd6"><rect x="0" y="1" width="8" height="8" rx="2"/><path d="M16 1l4 4-4 4-4-4z"/><path d="M25 2l5 3-5 3z"/></svg></span></div>
      </div>
    </div>
    <div class="row-actions">
      <svg width="17" height="17" viewBox="0 0 18 18" fill="none" stroke="#3277b5" stroke-width="1.7"><path d="M9 3H3v12h12V9M7 11l1-3 7-7 2 2-7 7z"/></svg><svg width="15" height="17" viewBox="0 0 14 16" fill="none" stroke="#e5533d" stroke-width="1.6"><path d="M1 3h12M5 3V1h4v2M2.5 3l1 12h7l1-12M5.5 6v6M8.5 6v6"/></svg>
      <svg width="17" height="17" viewBox="0 0 18 18" fill="none" stroke="#3277b5" stroke-width="1.7"><path d="M9 3H3v12h12V9M7 11l1-3 7-7 2 2-7 7z"/></svg><svg width="15" height="17" viewBox="0 0 14 16" fill="none" stroke="#e5533d" stroke-width="1.6"><path d="M1 3h12M5 3V1h4v2M2.5 3l1 12h7l1-12M5.5 6v6M8.5 6v6"/></svg>
      <svg width="17" height="17" viewBox="0 0 18 18" fill="none" stroke="#3277b5" stroke-width="1.7"><path d="M9 3H3v12h12V9M7 11l1-3 7-7 2 2-7 7z"/></svg><svg width="15" height="17" viewBox="0 0 14 16" fill="none" stroke="#e5533d" stroke-width="1.6"><path d="M1 3h12M5 3V1h4v2M2.5 3l1 12h7l1-12M5.5 6v6M8.5 6v6"/></svg>
      <svg width="17" height="17" viewBox="0 0 18 18" fill="none" stroke="#3277b5" stroke-width="1.7"><path d="M9 3H3v12h12V9M7 11l1-3 7-7 2 2-7 7z"/></svg><svg width="15" height="17" viewBox="0 0 14 16" fill="none" stroke="#e5533d" stroke-width="1.6"><path d="M1 3h12M5 3V1h4v2M2.5 3l1 12h7l1-12M5.5 6v6M8.5 6v6"/></svg>
    </div>
  </section>

  <section class="card collapsed" style="top:658px"><div class="obj-head">Asset<span class="chip remove"><svg width="10" height="10" viewBox="0 0 10 10" stroke="#e5533d" stroke-width="1.8"><path d="M1 1l8 8M9 1l-8 8"/></svg></span></div><svg class="chev" width="12" height="12" viewBox="0 0 12 12" fill="none" stroke="#16181d" stroke-width="1.8"><path d="M4 2l4 4-4 4"/></svg></section>
  <section class="card collapsed" style="top:718px"><div class="obj-head">Asset Relationship<span class="chip remove"><svg width="10" height="10" viewBox="0 0 10 10" stroke="#e5533d" stroke-width="1.8"><path d="M1 1l8 8M9 1l-8 8"/></svg></span></div><svg class="chev" width="12" height="12" viewBox="0 0 12 12" fill="none" stroke="#16181d" stroke-width="1.8"><path d="M4 2l4 4-4 4"/></svg></section>
  <section class="card collapsed" style="top:778px"><div class="obj-head">Asset Token Event<span class="chip remove"><svg width="10" height="10" viewBox="0 0 10 10" stroke="#e5533d" stroke-width="1.8"><path d="M1 1l8 8M9 1l-8 8"/></svg></span></div><svg class="chev" width="12" height="12" viewBox="0 0 12 12" fill="none" stroke="#16181d" stroke-width="1.8"><path d="M4 2l4 4-4 4"/></svg></section>
  <section class="card collapsed" style="top:838px"><div class="obj-head">Case<span class="chip remove"><svg width="10" height="10" viewBox="0 0 10 10" stroke="#e5533d" stroke-width="1.8"><path d="M1 1l8 8M9 1l-8 8"/></svg></span></div><svg class="chev" width="12" height="12" viewBox="0 0 12 12" fill="none" stroke="#16181d" stroke-width="1.8"><path d="M4 2l4 4-4 4"/></svg></section>
</main>
</body>
</html>
```